Rhythmic Gymnastics Web Design Built in Elementor - Mobile First (adaptable)

I am looking for an elite web designer to work with continuously.
Our goal with this contest is to find someone who can create custom designs (not from templates).
For this test we will be starting with one home page design and if we like the design we will move forward with you to work on more designs for the rest of the site and other sites
I have added a logo and brand colors of the company below.
Some images that can be used - https://files.quillbarrow.net/share/k7Tq2mWx9Lp4Rz
Brand guide - https://files.quillbarrow.net/share/v3Hn8cYd5Fb2Jm
Logo-
https://files.quillbarrow.net/share/p9Ws4eGt1Kx6Na
Name of company is Tavine Gymnastics
Some more images and company info - https://files.quillbarrow.net/share/r2Dm7uVz3Qc8Ye
Please make a mobile first design that can be adaptable for desktop
Navigation - Home, About, Schedule, Coaches, Facility, Results, Competitions, FAQ, Contact
Above the fold Hero **
Headline - LA's Elite Rhythmic Gymnastics - Confidence, Flexibility, Grace, & Results
Coach-led classes for ages 3-17. Flexible schedule. First session Free.
CTA - Free Trial
Trust Strip**
Program section (cards)**
Why choose us section**
Results/Social Proof Section**
testimonaial carousel
Schedule teaser section**
Pricing & Offers**
Coaches You'll Love section (cards)**
Facility Tour section**
Conversion Magnet (lead capture)**
A small box or band on the homepage that says:
“Not ready to book? Get our free Tavine First Steps Handbook.”
They enter Parent Name + Email + Child Age → they instantly get a helpful PDF and a friendly follow-up sequence. No hard sell.
FAQ's Section**
Location, hours, Parking section**
Map embed, service‑area chips (Granada Hills, Northridge, Chatsworth, etc.), hours table, contact block (Call, SMS, WhatsApp, Email, IG/TikTok).
Footer section with quick links**
Target Market(s)
That target market is parents of girls
Industry/Entity Type
Rhythmic Gymnastics

```html
<!DOCTYPE html>
<html lang="en">
<head>
<meta charset="utf-8">
<title>Tavine Gymnastics – Mobile Home Page</title>
<link href="https://fonts.googleapis.com/css2?family=Montserrat:wght@500;600;700;800&family=Poppins:wght@300;400;500;600&family=Pacifico&display=swap" rel="stylesheet">
<style>
:root{
  --navy:#1b2f6b;
  --navy-deep:#0f1a3d;
  --blue:#2f8fdc;
  --blue-mid:#3a9ee6;
  --sky:#4fb0ec;
  --ice:#e8f4fd;
  --ice-2:#f3f9fe;
  --ink:#1d2b4f;
  --muted:#6b7a93;
  --line:#d7e6f4;
  --white:#ffffff;
  --red:#d9343a;
}
*{box-sizing:border-box;margin:0;padding:0}
html,body{width:1200px;height:3715px;overflow:hidden;background:#fff}
body{position:relative;font-family:"Poppins",sans-serif;color:var(--ink)}
.col{position:absolute;top:87px;width:257px;overflow:hidden;background:#fff;box-shadow:0 2px 14px rgba(30,60,110,.12)}
.col-a{left:170px;height:3400px}
.col-b{left:472px;height:3201px}
.col-c{left:773px;height:2786px}
section{position:relative;overflow:hidden}
.photo{display:block}
.h2{font-family:"Montserrat",sans-serif;font-weight:700;font-size:14px;letter-spacing:1.6px;text-align:center;text-transform:uppercase;color:var(--ink);line-height:1.45}
.sub{font-size:10px;color:var(--muted);text-align:center;line-height:1.55;margin-top:6px;padding:0 14px}
.btn{display:block;margin:0 auto;border-radius:20px;font-family:"Montserrat",sans-serif;font-weight:600;font-size:10.5px;text-align:center;line-height:32px;height:32px}
.btn-fill{background:var(--blue);color:#fff;box-shadow:0 3px 8px rgba(47,143,220,.3)}
.btn-line{border:1.5px solid var(--blue);color:var(--blue);background:#fff}
.wave{position:absolute;left:0;width:257px;display:block}

/* header + hero */
.topbar{height:40px;display:flex;align-items:center;justify-content:space-between;padding:0 16px;background:#fff}
.brand{font-size:10px;font-weight:500;color:var(--navy)}
.burger{width:18px}
.burger i{display:block;height:1.5px;background:var(--ink);margin:3px 0}
.hero{height:464px;background:linear-gradient(#0c1533 0%,#142456 45%,#1f4a9a 100%);text-align:center;color:#fff}
.pill{display:inline-block;margin-top:28px;background:rgba(255,255,255,.12);border:1px solid rgba(255,255,255,.2);border-radius:10px;font-size:8px;letter-spacing:.6px;padding:2px 10px;color:#cdd8ee}
.hero h1{font-family:"Montserrat",sans-serif;font-weight:700;font-size:16px;letter-spacing:1.5px;line-height:1.35;margin-top:10px}
.hero .tag{font-family:"Montserrat",sans-serif;font-weight:700;font-size:10px;color:var(--sky);margin-top:5px}
.hero p{font-size:10px;line-height:1.45;margin:12px 22px 0}
.hero p b{font-weight:600}
.hero .btn{width:186px;margin-top:14px}
.hero .btn-dark{border:1.5px solid rgba(255,255,255,.75);color:#fff;margin-top:14px}
.hero-photo{position:absolute;left:0;top:248px;width:257px;height:216px;background:radial-gradient(ellipse at 50% 55%,#8fb0dc 0%,#4f7cc0 40%,rgba(31,74,154,0) 75%),linear-gradient(180deg,rgba(20,36,86,0) 0%,#3f6fb8 45%,#5d86c6 70%,#2a58a8 100%)}
.trust{height:245px;display:grid;grid-template-columns:1fr 1fr;padding:10px 10px 22px}
.trust-item{text-align:center;padding-top:14px;font-size:10px;color:var(--navy);line-height:1.3}
.trust-item:nth-child(1),.trust-item:nth-child(3){border-right:1px solid var(--line)}
.badge{width:46px;height:46px;margin:0 auto 6px;display:block}

/* programs */
.programs{height:1370px;background:linear-gradient(#e4f1fc,#f4f9fe 30%,#fff);padding-top:20px}
.prog{width:229px;margin:0 auto;background:#fff;border-radius:6px;overflow:hidden;box-shadow:0 2px 8px rgba(30,60,110,.1);border-bottom:3px solid var(--blue);position:relative;height:300px;margin-top:16px}
.prog:first-of-type{margin-top:18px}
.prog .photo{height:166px}
.prog .arrow{position:absolute;right:12px;top:144px;width:26px;height:26px;border-radius:50%;background:var(--blue);border:2px solid #fff;display:flex;align-items:center;justify-content:center}
.prog .age{position:absolute;left:14px;top:158px;background:#fff;color:var(--blue);font-size:8.5px;padding:1px 8px;border-radius:8px}
.prog h3{font-family:"Montserrat",sans-serif;font-weight:700;font-size:13px;color:var(--navy);padding:14px 18px 0}
.prog p{font-size:9.6px;color:var(--muted);line-height:1.7;padding:10px 18px 0}
.ribbon-band{height:335px;background:radial-gradient(ellipse at 55% 45%,#d9343a 0%,rgba(217,52,58,.55) 12%,rgba(217,52,58,0) 30%),linear-gradient(180deg,#fff 0%,#fff 12%,#2a4f95 40%,#3b7fd0 80%,#4a9ee6 100%)}
.why{height:946px;background:linear-gradient(#4aa3e6,#3a92de 60%,#2f84d4);color:#fff;text-align:center;padding-top:4px}
.why .h2{color:#fff}
.why .sub{color:#e6f2fc}
.why-card{width:182px;height:184px;margin:12px auto 0;border:1.5px solid rgba(255,255,255,.35);border-radius:6px;background:rgba(255,255,255,.08);padding:20px 10px 0}
.why-card:first-of-type{margin-top:24px}
.why-icon{width:52px;height:52px;border-radius:50%;background:rgba(255,255,255,.92);margin:0 auto;display:flex;align-items:center;justify-content:center;box-shadow:0 0 0 5px rgba(255,255,255,.25)}
.why-card h3{font-family:"Montserrat",sans-serif;font-weight:700;font-size:13px;margin-top:12px}
.why-card p{font-size:9.6px;line-height:1.65;margin-top:6px;color:#e8f3fd}

/* testimonials */
.reviews{height:433px;padding-top:38px;background:#fff}
.stars{text-align:center;color:var(--blue);font-size:16px;letter-spacing:2px;margin-top:16px}
.quote-box{width:212px;margin:4px auto 0;position:relative;height:160px;border-radius:6px;box-shadow:0 2px 8px rgba(30,60,110,.08);padding:10px 22px}
.quote-box p{font-size:9.8px;font-style:italic;color:var(--muted);line-height:1.95;text-align:center}
.nav-dot{position:absolute;top:40px;width:22px;height:22px;border-radius:50%;border:1px solid var(--blue);background:#fff}
.nav-l{left:-10px}.nav-r{right:-10px}
.nav-dot svg{display:block;margin:5px}
.author{display:flex;align-items:center;gap:8px;margin:10px 0 0 52px}
.avatar{width:34px;height:34px;border-radius:50%;background:linear-gradient(#d8b9a0,#9a7a66);border:2px solid #fff;box-shadow:0 0 0 1px var(--line)}
.author b{display:block;font-size:10px;font-weight:500;color:var(--navy)}
.author span{font-size:9.5px;color:var(--muted)}
.dots{display:flex;gap:5px;justify-content:center;margin-top:14px}
.dots i{width:5px;height:5px;border-radius:50%;background:#c7dcee}
.dots i.on{width:20px;border-radius:3px;background:var(--blue)}
.schedule{height:577px;background:var(--ice);padding-top:62px}
.days{width:215px;margin:18px auto 0;background:#d6ebfa;border-radius:8px;padding:10px;}
.day{height:52px;background:#fff;border-radius:6px;text-align:center;margin-bottom:13px;padding-top:10px}
.day:last-child{margin-bottom:0}
.day b{display:block;font-size:12px;font-weight:500;color:var(--navy)}
.day span{font-size:9.6px;color:var(--muted)}
.schedule .btn{width:186px;margin-top:18px}
.pricing{height:1363px;background:linear-gradient(#f6fafe,#eaf4fd);padding-top:38px}
.plan{width:217px;margin:26px auto 0;background:#fff;border-radius:8px;box-shadow:0 3px 10px rgba(30,60,110,.1);overflow:hidden;position:relative}
.plan-head{position:relative;height:118px;text-align:center;padding-top:18px;background:var(--ice-2)}
.plan-head h3{font-family:"Montserrat",sans-serif;font-weight:500;font-size:16px;color:var(--navy);letter-spacing:.5px}
.price{font-size:24px;color:var(--blue);margin-top:2px}
.price small{font-size:10px;color:var(--muted)}
.plan-head p{font-size:10px;color:var(--navy);line-height:1.5}
.plan ul{list-style:none;padding:22px 22px 0}
.plan li{font-size:10.2px;color:var(--muted);line-height:27px;padding-left:20px;position:relative}
.plan li:before{content:"";position:absolute;left:2px;top:10px;width:8px;height:4px;border-left:1.5px solid var(--blue);border-bottom:1.5px solid var(--blue);transform:rotate(-45deg)}
.plan .btn{width:186px;margin-top:16px}
.plan-hot .plan-head{background:var(--navy);height:162px;padding-top:14px}
.plan-hot .plan-head h3,.plan-hot .plan-head p{color:#fff}
.plan-hot .price{color:var(--sky)}
.plan-hot .price small{color:#dfe8f7}
.hot-tag{display:inline-block;background:var(--blue);color:#fff;font-size:8.5px;padding:2px 10px;border-radius:3px;margin-bottom:6px}
.coaches{height:382px;background:linear-gradient(#2a6fc2,#3791de);padding-top:36px}
.coaches .h2,.coaches .sub{color:#fff}
.coach{position:absolute;left:21px;top:110px;width:184px;height:209px;border-radius:6px;overflow:hidden;background:#4c8fd4}
.coach .photo{height:162px}
.coach b{display:block;text-align:center;color:#fff;font-size:12px;font-weight:500;margin-top:10px}
.coach span{display:block;text-align:center;color:#bcd8f4;font-size:9px}
.coach-peek{position:absolute;left:218px;top:110px;width:60px;height:209px;border-radius:6px;background:#4c8fd4}
.coaches .dots{position:absolute;left:0;right:0;top:340px}
.coaches .dots i{background:rgba(255,255,255,.5)}.coaches .dots i.on{background:#fff}
.studio{height:447px;padding-top:44px;background:#fff}
.gallery{display:grid;grid-template-columns:107px 107px;gap:8px;justify-content:center;margin-top:16px}
.gallery .photo{height:104px;border-radius:3px}
.studio .btn{width:186px;margin-top:22px}

/* lead capture */
.lead{height:502px;background:linear-gradient(#fff 0%,var(--ice) 40%,#dcecfa);padding-top:88px}
.lead .sub a{color:var(--blue);text-decoration:none}
.form{padding:14px 26px 0}
.form label{display:block;font-size:9.5px;font-weight:500;color:var(--navy);margin-top:10px}
.field{height:32px;background:#fff;border-radius:5px;margin-top:8px;font-size:9.5px;color:var(--muted);line-height:32px;padding-left:18px;border:1px solid #edf3f9}
.lead .btn{width:206px;margin-top:26px;height:36px;line-height:36px;font-size:11.5px}
.privacy{font-size:8.8px;color:var(--muted);text-align:center;margin-top:12px;font-weight:500}
.faq{height:652px;background:linear-gradient(#3f8fdc,#4ba4e8 50%,#3f96e0)}
.faq-photo{height:178px;background:radial-gradient(ellipse at 30% 55%,rgba(217,52,58,.7) 0%,rgba(217,52,58,0) 30%),radial-gradient(ellipse at 65% 40%,#e9f0f8 0%,rgba(233,240,248,0) 25%),linear-gradient(135deg,#1c3d86,#2f6fc8 45%,#7aa9d9 70%,#2756a6)}
.faq .h2{color:#fff;margin-top:8px}
.faq .sub{color:#eef6fd;font-weight:500}
.q{width:218px;margin:12px auto 0;background:#fff;border-radius:5px;font-size:10px;font-weight:600;color:var(--navy);padding:10px 28px 10px 22px;line-height:1.6;position:relative}
.q:after{content:"";position:absolute;right:14px;top:50%;width:4px;height:4px;border-right:1px solid var(--muted);border-bottom:1px solid var(--muted);transform:translateY(-70%) rotate(45deg)}
.visit{height:721px;background:linear-gradient(#fff,#eef6fd);padding-top:26px}
.map{width:200px;height:220px;margin:18px auto 0;border-radius:4px;background:linear-gradient(135deg,#d9e9c9,#eef0e4 40%,#e6ead8 70%,#dbe6f2);border:4px solid #fff;box-shadow:0 2px 8px rgba(30,60,110,.15)}
.chip{width:188px;height:32px;margin:10px auto 0;border:1.5px solid var(--blue);border-radius:16px;text-align:center;font-size:10.5px;font-weight:500;color:var(--blue);line-height:29px;background:#fff}
.chip:first-of-type{margin-top:24px}
.pin{display:block;margin:26px auto 0}
.visit h3{font-size:13px;font-weight:500;color:var(--navy);text-align:center;margin-top:10px}
.visit p{font-size:9.8px;color:var(--muted);text-align:center;line-height:1.8;padding:0 26px;margin-top:8px}
.visit .btn{width:186px;margin-top:24px}
.footer{height:911px;background:linear-gradient(#24458f,#1c3676 40%,var(--navy))}
.foot-photo{height:300px;background:radial-gradient(ellipse at 50% 50%,#1a2a55 0%,rgba(26,42,85,.6) 15%,rgba(26,42,85,0) 32%),linear-gradient(180deg,#fff 0%,#fff 6%,#2d5bb0 26%,#3c6ec0 60%,#2a4f9c 100%)}
.foot-brand{font-size:15px;font-weight:500;color:#fff;text-align:center;margin-top:2px}
.foot-text{font-size:9.6px;color:#e3eaf8;text-align:center;line-height:1.45;padding:0 22px;margin-top:12px;font-weight:500}
.socials{display:flex;gap:12px;justify-content:center;margin-top:20px}
.socials i{width:20px;height:20px;border-radius:50%;border:1px solid rgba(255,255,255,.5)}
.links{display:grid;grid-template-columns:1fr 1fr;padding:30px 44px 0 44px}
.links h4{font-size:10.5px;font-weight:500;color:#fff;margin-bottom:12px}
.links a{display:block;font-size:9.5px;color:#cfdaf0;text-decoration:none;line-height:24px}
.contact{padding:24px 44px 0}
.contact h4{font-size:10.5px;font-weight:500;color:#fff}
.c-row{display:flex;gap:12px;margin-top:14px}
.c-ico{width:20px;height:20px;border-radius:50%;background:#fff;flex:none;display:flex;align-items:center;justify-content:center}
.c-row b{display:block;font-size:9.5px;font-weight:400;color:#fff}
.c-row span{font-size:9.5px;color:#cfdaf0}
.copy{margin:30px 22px 0;border-top:1px solid rgba(255,255,255,.2);padding-top:16px;text-align:center;font-size:8.5px;color:#aebedf}
.thanks{position:absolute;left:40px;top:3560px;font-family:"Pacifico",cursive;font-size:50px;color:#2878c9}
</style>
</head>
<body>

<div class="col col-a">
  <div class="topbar">
    <span class="brand">Tavine Gymnastics</span>
    <span class="burger"><i></i><i></i><i></i></span>
  </div>
  <section class="hero">
    <div class="hero-photo photo" role="img" aria-label="Rhythmic gymnasts performing with ribbons on a lit competition floor"></div>
    <div style="position:relative">
      <span class="pill">SCHOOL OF CHAMPIONS</span>
      <h1>LA'S ELITE RHYTHMIC<br>GYMNASTICS</h1>
      <div class="tag">Confidence, Flexibility, Grace, &amp; Results</div>
      <p>Coach-led classes for ages 3-17. Flexible schedule. First session <b>Free</b>.</p>
      <a class="btn btn-fill">Free Trial</a>
      <a class="btn btn-dark">Call Now</a>
    </div>
    <svg class="wave" style="bottom:-1px" height="40" viewBox="0 0 257 40" preserveAspectRatio="none"><path d="M0 22 C70 40 170 40 257 6 L257 14 C170 44 70 44 0 28Z" fill="#2f8fdc"/><path d="M0 28 C70 46 170 46 257 14 L257 40 L0 40Z" fill="#fff"/></svg>
  </section>

  <section class="trust">
    <div class="trust-item"><svg class="badge" viewBox="0 0 46 46"><circle cx="23" cy="23" r="21" fill="#2f8fdc"/><circle cx="23" cy="23" r="17" fill="none" stroke="#fff" stroke-opacity=".35"/><circle cx="23" cy="19" r="4" fill="none" stroke="#fff" stroke-width="1.6"/><path d="M18 31 v-4 h10 v4" fill="none" stroke="#fff" stroke-width="1.6"/></svg>Ex-Olympian<br>Coaches</div>
    <div class="trust-item"><svg class="badge" viewBox="0 0 46 46"><circle cx="23" cy="23" r="21" fill="#2f8fdc"/><circle cx="23" cy="23" r="17" fill="none" stroke="#fff" stroke-opacity=".35"/><circle cx="20" cy="19" r="3.5" fill="none" stroke="#fff" stroke-width="1.6"/><circle cx="27" cy="20" r="3" fill="none" stroke="#fff" stroke-width="1.6"/><path d="M14 30 q6-7 12 0 M24 29 q5-6 9 1" fill="none" stroke="#fff" stroke-width="1.6"/></svg>National Team<br>Experience</div>
    <div class="trust-item"><svg class="badge" viewBox="0 0 46 46"><circle cx="23" cy="23" r="21" fill="#2f8fdc"/><circle cx="23" cy="23" r="17" fill="none" stroke="#fff" stroke-opacity=".35"/><rect x="15" y="16" width="16" height="14" rx="2" fill="none" stroke="#fff" stroke-width="1.6"/><path d="M15 21 h16 M19 14 v4 M27 14 v4" stroke="#fff" stroke-width="1.6"/></svg>Over 10 Years<br>of Excellence</div>
    <div class="trust-item"><svg class="badge" viewBox="0 0 46 46"><circle cx="23" cy="23" r="21" fill="#2f8fdc"/><circle cx="23" cy="23" r="17" fill="none" stroke="#fff" stroke-opacity=".35"/><rect x="15" y="20" width="16" height="11" fill="none" stroke="#fff" stroke-width="1.6"/><path d="M14 17 h18 v3 h-18z M23 17 v14" fill="none" stroke="#fff" stroke-width="1.6"/></svg>First Class<br>Free</div>
  </section>

  <section class="programs">
    <h2 class="h2">Our Programs</h2>
    <p class="sub">Age-appropriate classes designed to nurture every gymnast from beginner to champion</p>
    <article class="prog"><div class="photo" role="img" aria-label="Young girl practicing in a bright gym" style="background:linear-gradient(135deg,#6d90c2,#cfdff0 55%,#9ab8dc)"></div><span class="arrow"><svg width="10" height="10" viewBox="0 0 10 10"><path d="M2 5h6M5 2l3 3-3 3" fill="none" stroke="#fff" stroke-width="1.3"/></svg></span><span class="age">Ages 3-5</span><h3>Little Stars</h3><p>Introduction to rhythmic gymnastics through play and movement. Build coordination, flexibility, and confidence.</p></article>
    <article class="prog"><div class="photo" role="img" aria-label="Group of girls stretching during a class" style="background:linear-gradient(135deg,#5b7fb8,#d9e5f2 55%,#7f9fce)"></div><span class="arrow"><svg width="10" height="10" viewBox="0 0 10 10"><path d="M2 5h6M5 2l3 3-3 3" fill="none" stroke="#fff" stroke-width="1.3"/></svg></span><span class="age">Ages 6-9</span><h3>Rising Athletes</h3><p>Develop fundamental skills with ribbons, hoops, and balls. Focus on technique and artistic expression.</p></article>
    <article class="prog"><div class="photo" role="img" aria-label="Teen gymnasts training arm positions together" style="background:linear-gradient(135deg,#3f7d52,#cfd9cc 55%,#5f8e68)"></div><span class="arrow"><svg width="10" height="10" viewBox="0 0 10 10"><path d="M2 5h6M5 2l3 3-3 3" fill="none" stroke="#fff" stroke-width="1.3"/></svg></span><span class="age">Ages 10-13</span><h3>Elite Performance</h3><p>Advanced training for competitive athletes. Master all apparatus and prepare for regional competitions.</p></article>
    <article class="prog"><div class="photo" role="img" aria-label="Competitive gymnasts in leotards training with coach" style="background:linear-gradient(135deg,#6b84b8,#e2e8f2 55%,#8fa9d2)"></div><span class="arrow"><svg width="10" height="10" viewBox="0 0 10 10"><path d="M2 5h6M5 2l3 3-3 3" fill="none" stroke="#fff" stroke-width="1.3"/></svg></span><span class="age">Ages 14-17</span><h3>Champions Track</h3><p>High-level competitive training with ex-Olympian coaches. National team preparation and college recruitment support.</p></article>
  </section>

  <section class="ribbon-band photo" role="img" aria-label="Gymnast in a red leotard performing a ribbon leap"></section>
  <section class="why">
    <h2 class="h2">Why Choose Tavine<br>Gymnastics?</h2>
    <p class="sub">We're not just a gymnastics school – we're a community dedicated to developing champions in sport and in life.</p>
    <div class="why-card"><div class="why-icon"><svg width="24" height="24" viewBox="0 0 24 24" fill="none" stroke="#2f8fdc" stroke-width="1.6"><path d="M7 4h10v5a5 5 0 0 1-10 0z M7 6H4a3 3 0 0 0 3 4 M17 6h3a3 3 0 0 1-3 4 M12 14v4 M8 20h8"/></svg></div><h3>Proven Results</h3><p>Our athletes consistently win at regional and national competitions</p></div>
    <div class="why-card"><div class="why-icon"><svg width="24" height="24" viewBox="0 0 24 24" fill="none" stroke="#2f8fdc" stroke-width="1.6"><rect x="4" y="5" width="16" height="15" rx="2"/><path d="M4 10h16 M8 3v4 M16 3v4"/><circle cx="12" cy="15" r="2.5"/></svg></div><h3>Flexible Schedule</h3><p>Multiple class times throughout the week to fit your family's needs</p></div>
    <div class="why-card"><div class="why-icon"><svg width="24" height="24" viewBox="0 0 24 24" fill="none" stroke="#2f8fdc" stroke-width="1.6"><circle cx="14" cy="5" r="2"/><path d="M5 9h14 M12 9l-2 6h4l2 5 M10 15l-4 4"/></svg></div><h3>Expert Coaching</h3><p>Learn from ex-Olympians and national team coaches with decades of experience</p></div>
    <div class="why-card"><div class="why-icon"><svg width="24" height="24" viewBox="0 0 24 24" fill="none" stroke="#2f8fdc" stroke-width="1.6"><rect x="9" y="4" width="6" height="5"/><path d="M4 20V14h5v6 M9 20V11h6v9 M15 20v-4h5v4 M3 20h18"/></svg></div><h3>Build Confidence</h3><p>Watch your daughter grow in grace, strength, and self-assurance</p></div>
  </section>
</div>

<div class="col col-b">
  <section class="reviews">
    <h2 class="h2">Real Results, Real<br>Confidence</h2>
    <p class="sub">Hear from parents whose daughters have transformed through our program</p>
    <div class="stars">★★★★★</div>
    <div class="quote-box">
      <span class="nav-dot nav-l"><svg width="10" height="10" viewBox="0 0 10 10"><path d="M6 2L3 5l3 3" fill="none" stroke="#2f8fdc" stroke-width="1.2"/></svg></span>
      <span class="nav-dot nav-r"><svg width="10" height="10" viewBox="0 0 10 10"><path d="M4 2l3 3-3 3" fill="none" stroke="#2f8fdc" stroke-width="1.2"/></svg></span>
      <p>"Lila has blossomed since joining Tavine Gymnastics. Her confidence has soared, and she's made wonderful friends. The coaches are incredibly skilled and nurturing."</p>
    </div>
    <div class="author"><span class="avatar" role="img" aria-label="Parent portrait"></span><div><b>Dana Whitfield</b><span>Mother of Lila, 8</span></div></div>
    <div class="dots"><i class="on"></i><i></i><i></i><i></i><i></i></div>
  </section>

  <section class="schedule">
    <svg class="wave" style="top:0" height="46" viewBox="0 0 257 46" preserveAspectRatio="none"><path d="M0 0H257V10 C180 40 80 40 0 8Z" fill="#fff"/><path d="M0 8 C80 40 180 40 257 10" fill="none" stroke="#2f8fdc" stroke-width="4"/></svg>
    <svg style="position:absolute;left:114px;top:14px" width="28" height="28" viewBox="0 0 28 28"><circle cx="14" cy="14" r="13" fill="#2f8fdc" stroke="#fff" stroke-width="2"/><circle cx="14" cy="14" r="6" fill="none" stroke="#fff" stroke-width="1.4"/><path d="M14 10v4l2.5 2" fill="none" stroke="#fff" stroke-width="1.4"/></svg>
    <h2 class="h2">Flexible Weekly<br>Schedule</h2>
    <p class="sub">Multiple class times to fit your family's busy life</p>
    <div class="days">
      <div class="day"><b>Monday</b><span>4:00 PM - 8:00 PM</span></div>
      <div class="day"><b>Tuesday</b><span>4:00 PM - 8:00 PM</span></div>
      <div class="day"><b>Wednesday</b><span>4:00 PM - 8:00 PM</span></div>
      <div class="day"><b>Thursday</b><span>4:00 PM - 8:00 PM</span></div>
      <div class="day"><b>Saturday</b><span>9:00 AM - 2:00 PM</span></div>
    </div>
    <a class="btn btn-fill">See Full Schedule</a>
  </section>

  <section class="pricing">
    <h2 class="h2">Pricing &amp; Offers</h2>
    <p class="sub">Flexible options to match your goals and budget</p>
    <div class="plan" style="height:346px">
      <div class="plan-head"><h3>DROP-IN</h3><div class="price">$35 <small>per class</small></div><p>Perfect for trying us out</p>
        <svg class="wave" style="bottom:0" height="26" viewBox="0 0 217 26" preserveAspectRatio="none"><path d="M0 6 C70 22 150 22 217 2 V26 H0Z" fill="#fff"/><path d="M0 6 C70 22 150 22 217 2" fill="none" stroke="#2f8fdc" stroke-width="4"/></svg></div>
      <ul><li>Single class access</li><li>All equipment provided</li><li>Expert instruction</li><li>Flexible scheduling</li></ul>
      <a class="btn btn-line">Get Started</a>
    </div>
    <div class="plan plan-hot" style="height:400px">
      <div class="plan-head"><span class="hot-tag">Most Popular</span><h3>MONTHLY</h3><div class="price">$240 <small>per month</small></div><p>Best value for<br>committed athletes</p>
        <svg class="wave" style="bottom:0" height="22" viewBox="0 0 217 22" preserveAspectRatio="none"><path d="M0 6 C70 20 150 20 217 2 V22 H0Z" fill="#fff"/><path d="M0 6 C70 20 150 20 217 2" fill="none" stroke="#2f8fdc" stroke-width="4"/></svg></div>
      <ul><li>8 classes per month</li><li>Priority scheduling</li><li>Free trial class</li><li>Competition prep included</li><li>Performance evaluations</li></ul>
      <a class="btn btn-fill" style="margin-top:22px">Get Started</a>
    </div>
    <div class="plan" style="height:397px">
      <div class="plan-head"><h3>UNLIMITED</h3><div class="price">$450 <small>per month</small></div><p>For serious competitors</p>
        <svg class="wave" style="bottom:0" height="26" viewBox="0 0 217 26" preserveAspectRatio="none"><path d="M0 6 C70 22 150 22 217 2 V26 H0Z" fill="#fff"/><path d="M0 6 C70 22 150 22 217 2" fill="none" stroke="#2f8fdc" stroke-width="4"/></svg></div>
      <ul><li>Unlimited classes</li><li>Private coaching sessions</li><li>Competition team eligible</li><li>Nutrition guidance</li><li>Free trial class</li><li>College recruitment support</li></ul>
      <a class="btn btn-line">Get Started</a>
    </div>
  </section>

  <section class="coaches">
    <h2 class="h2">Coaches You'll Love</h2>
    <p class="sub">Learn from world-class athletes and certified instructors</p>
    <div class="coach"><div class="photo" role="img" aria-label="Head coach portrait" style="background:linear-gradient(#c9c3bd,#8d8680)"></div><b>Alina Voss</b><span>Head Coach &amp; Founder</span></div>
    <div class="coach-peek"></div>
    <div class="dots"><i class="on"></i><i></i><i></i><i></i><i></i></div>
  </section>

  <section class="studio">
    <h2 class="h2">Take a Peek Inside<br>Our Studio</h2>
    <p class="sub">A state-of-the-art facility designed for champions</p>
    <div class="gallery">
      <div class="photo" role="img" aria-label="Gymnast with ribbon in the studio" style="background:linear-gradient(135deg,#2d3d78,#c9506b 60%,#e0c7d3)"></div>
      <div class="photo" role="img" aria-label="Gymnasts training on the floor" style="background:linear-gradient(135deg,#dfe8f0,#9fb3c8 60%,#c1cfdc)"></div>
      <div class="photo" role="img" aria-label="Ribbon routine in the main hall" style="background:linear-gradient(135deg,#2f5fb4,#7f9cc8 60%,#d7a3b0)"></div>
      <div class="photo" role="img" aria-label="Athletes warming up in the gym" style="background:linear-gradient(135deg,#c9cfd8,#8fa6c4 60%,#d0c3c8)"></div>
    </div>
    <a class="btn btn-fill">See All Gallery</a>
  </section>
</div>

<div class="col col-c">
  <section class="lead">
    <svg class="wave" style="top:0" height="60" viewBox="0 0 257 60" preserveAspectRatio="none"><path d="M0 0H257V20 C180 50 80 50 0 20Z" fill="#fff"/><path d="M0 20 C80 50 180 50 257 20" fill="none" stroke="#2f8fdc" stroke-width="4"/></svg>
    <svg style="position:absolute;left:114px;top:34px" width="28" height="28" viewBox="0 0 28 28"><circle cx="14" cy="14" r="13" fill="#2f8fdc" stroke="#fff" stroke-width="2"/><path d="M14 8v9 M10 13l4 4 4-4 M9 20h10" fill="none" stroke="#fff" stroke-width="1.5"/></svg>
    <h2 class="h2">Not Ready to Book?</h2>
    <p class="sub">Get our free <a>Tavine First Steps Handbook</a> – tips, exercises, and what to expect in your first class.</p>
    <div class="form">
      <label>Parent Name</label><div class="field">Your name</div>
      <label>Email</label><div class="field">your@email.com</div>
      <label>Child's Age</label><div class="field">Age</div>
    </div>
    <a class="btn btn-fill">Download Free Guide</a>
    <p class="privacy">We respect your privacy. Unsubscribe anytime.</p>
  </section>

  <section class="faq">
    <div class="faq-photo photo" role="img" aria-label="Gymnast balancing with a ribbon against a blue backdrop"></div>
    <h2 class="h2">Frequently Asked<br>Questions</h2>
    <p class="sub">Everything parents want to know about our programs</p>
    <div class="q">What should my daughter wear to her first class?</div>
    <div class="q">Do you offer a free trial class?</div>
    <div class="q">What ages do you accept?</div>
    <div class="q">How often should my child attend classes?</div>
    <div class="q">Is rhythmic gymnastics safe?</div>
    <div class="q">Can my daughter join if she has no experience?</div>
  </section>

  <section class="visit">
    <h2 class="h2">Visit Us</h2>
    <p class="sub" style="color:var(--muted);padding:0 34px">Located in the heart of the San Fernando Valley</p>
    <div class="map photo" role="img" aria-label="Street map showing 48 Meadowlark Way, Granada Hills, CA"></div>
    <div class="chip">Granada Hills</div>
    <div class="chip">Northridge</div>
    <div class="chip">Chatsworth</div>
    <svg class="pin" width="26" height="32" viewBox="0 0 26 32"><path d="M13 30 C5 20 3 15 3 11 a10 10 0 0 1 20 0 c0 4-2 9-10 19z" fill="none" stroke="#2f8fdc" stroke-width="2"/><circle cx="13" cy="11" r="4" fill="none" stroke="#2f8fdc" stroke-width="2"/></svg>
    <h3>Parking &amp; Access</h3>
    <p>Free parking available in our private lot. ADA accessible entrance at the main door. Easy access from the 118 and 405 freeways.</p>
    <a class="btn btn-fill">Schedule Your Free Trial</a>
  </section>

  <footer class="footer">
    <div class="foot-photo photo" role="img" aria-label="Gymnast in a sparkling leotard holding a ribbon stick overhead"></div>
    <div class="foot-brand">Tavine Gymnastics</div>
    <p class="foot-text">LA's premier rhythmic gymnastics school, developing champions since 2013. Building confidence, grace, and excellence one athlete at a time.</p>
    <div class="socials"><i></i><i></i><i></i><i></i></div>
    <div class="links">
      <div><h4>Quick Links</h4><a>Home</a><a>About</a><a>Programs</a><a>Schedule</a></div>
      <div><h4>More</h4><a>Coaches</a><a>Facility</a><a>FAQ</a><a>Contact</a></div>
    </div>
    <div class="contact">
      <h4>Contact Us</h4>
      <div class="c-row"><span class="c-ico"><svg width="10" height="10" viewBox="0 0 10 10"><path d="M2 1h2l1 2-1 1a5 5 0 0 0 2 2l1-1 2 1v2a1 1 0 0 1-1 1A7 7 0 0 1 1 2a1 1 0 0 1 1-1z" fill="#1b2f6b"/></svg></span><div><b>Phone</b><span>+1 (818) 555 0142</span></div></div>
      <div class="c-row"><span class="c-ico"><svg width="10" height="10" viewBox="0 0 10 10"><rect x="1" y="2" width="8" height="6" fill="none" stroke="#1b2f6b"/><path d="M1 2l4 3 4-3" fill="none" stroke="#1b2f6b"/></svg></span><div><b>Email</b><span>hello@tavinegym.com</span></div></div>
      <div class="c-row"><span class="c-ico"><svg width="10" height="10" viewBox="0 0 10 10"><path d="M5 9C2 6 2 5 2 4a3 3 0 0 1 6 0c0 1 0 2-3 5z" fill="#1b2f6b"/></svg></span><div><b>Location</b><span>Granada Hills, CA</span></div></div>
    </div>
    <p class="copy">© 2025 Tavine Gymnastics. All rights reserved.</p>
  </footer>
</div>

<div class="thanks">Thanks for watching</div>
</body>
</html>
```